Laboratory and geotechnical service provider needs Word template

We require a new Word Template for our business. We are looking for a modern, business-like format. We typically generate reports such as management plans, business plans, method statements, technical reports. These reports cover generally between 5 and 30 pages, but sometimes up to 500 pages including the appendices.

Lab reports have their own formats and are not parts of this scope.

Target Market(s)

We report to Clients such as construction industry contractors, governmental departments and engineering consultants.

Industry/Entity Type

Technical Service

Colors

Designer to choose colors to be used in the design.

Requirements
Must have
• The report needs a fancy cover page with a title field, subtitle, project field, client name field, reference number field. Photo/graphics as background on cover. Second page needs a revision table for document control. Table of contents up to 2 levels. Appendices to be part of TOC. Report first page with custom headings for body text, titles, subtitles, headings 1, 2, 3, etc. Include a table with caption, figure with caption, bullet list, numbered list. Appendix page. Please use fonts consistently, choose a common, but professional, modern font.
Nice to have
• We traditionally use black and yellow as company colours. Please visit our company page www.harbentestworks.com.
Should not have
• The two attached word documents is what we use now for your information, we are looking for something better!

```html
<!DOCTYPE html>
<html lang="en">
<head>
<meta charset="utf-8">
<title>Harben Test Works – Table of Contents</title>
<link href="https://fonts.googleapis.com/css2?family=Anton&family=Arimo:wght@700&display=swap" rel="stylesheet">
<style>
  :root {
    --page-dark: #232323;
    --edge-blue: #3d5f80;
    --brand-yellow: #fcee0c;
    --ink: #0a0a0a;
    --photo-sky: #5c6683;
    --photo-mid: #4d4f5e;
    --photo-ground: #5a5560;
  }
  html, body {
    margin: 0;
    padding: 0;
    overflow: hidden;
    background: var(--page-dark);
  }
  .page {
    position: relative;
    width: 927px;
    height: 1200px;
    background: var(--page-dark);
    overflow: hidden;
  }
  .page-edge {
    position: absolute;
    top: 0;
    bottom: 0;
    width: 2px;
    background: var(--edge-blue);
  }
  .page-edge--left { left: 0; }
  .page-edge--right { right: 2px; }
  .feature-band {
    position: absolute;
    left: 0;
    top: 182px;
    width: 927px;
    height: 860px;
    display: flex;
  }
  .site-photo {
    width: 287px;
    height: 100%;
    background: linear-gradient(180deg, var(--photo-sky) 0%, #585f79 45%, var(--photo-mid) 72%, var(--photo-ground) 100%);
    border-right: 1px solid #6b6a3a;
  }
  .contents-panel {
    flex: 1;
    background: var(--brand-yellow);
    position: relative;
  }
  .contents-title {
    position: absolute;
    left: 87px;
    top: 198px;
    margin: 0;
    font-family: "Anton", "Oswald", sans-serif;
    font-weight: 400;
    font-size: 43px;
    line-height: 1;
    color: var(--ink);
    letter-spacing: 0.2px;
  }
  .contents-list {
    position: absolute;
    left: 90px;
    top: 278px;
    width: 403px;
    margin: 0;
    padding: 0;
    list-style: none;
    font-family: "Arimo", Arial, sans-serif;
    font-weight: 700;
    font-size: 20px;
    color: var(--ink);
  }
  .contents-entry {
    display: flex;
    align-items: baseline;
    height: 28px;
    line-height: 28px;
    white-space: nowrap;
  }
  .entry-number { width: 36px; }
  .entry-leader {
    flex: 1;
    overflow: hidden;
    margin-left: 6px;
    letter-spacing: 1px;
  }
  .entry-leader::after {
    content: "..................................................";
  }
</style>
</head>
<body>
  <div class="page">
    <div class="page-edge page-edge--left"></div>
    <div class="page-edge page-edge--right"></div>
    <section class="feature-band">
      <div class="site-photo" role="img" aria-label="Photograph of a red drilling rig on a city waterfront site with palm trees and towers behind"></div>
      <div class="contents-panel">
        <h1 class="contents-title">TABLE OF CONTENTS</h1>
        <ol class="contents-list">
          <li class="contents-entry"><span class="entry-number">01.</span><span class="entry-name">INTRODUCTION</span><span class="entry-leader"></span><span class="entry-page">01</span></li>
          <li class="contents-entry"><span class="entry-number">02.</span><span class="entry-name">INTRODUCTION</span><span class="entry-leader"></span><span class="entry-page">01</span></li>
          <li class="contents-entry"><span class="entry-number">03.</span><span class="entry-name">INTRODUCTION</span><span class="entry-leader"></span><span class="entry-page">01</span></li>
          <li class="contents-entry"><span class="entry-number">04.</span><span class="entry-name">INTRODUCTION</span><span class="entry-leader"></span><span class="entry-page">01</span></li>
          <li class="contents-entry"><span class="entry-number">05.</span><span class="entry-name">INTRODUCTION</span><span class="entry-leader"></span><span class="entry-page">01</span></li>
          <li class="contents-entry"><span class="entry-number">06.</span><span class="entry-name">INTRODUCTION</span><span class="entry-leader"></span><span class="entry-page">01</span></li>
        </ol>
      </div>
    </section>
  </div>
</body>
</html>
```